Building and Facilities Management brochure

Please refer to attached PDF, page by page with information about the brief.
SOPHISTICATED, BOLD, PROFESSIONAL BROCHURE to market our company in business meetings to Builders, Owners of buildings, Strata Committees etc.

The final design should portray quality, service, integrity,
Clear Communication

Attached is:
- pdf with details of basic layout options and wording and most of the information about the brief.
- Logo options to use
- Business card designs to understand what design we have previously had.
- Word document of the pdf if that helps to copy the information.

Target Market(s)

Professionals. Builders/developer, Strata Owners, and Building owners who want a high level of service and management of their building

Industry/Entity Type

It Company

Requirements
Must have
• - Logo
• - Contact details
• - Use of the colour in the design which has been specified.
• - Images/s of building/s
• - Use the phrase "Quality Service with Integrity"
Nice to have
• - as much of the wording as possible from the document which was uploaded, that will fit and work with the design
Should not have
• Excessive colour or variances as it needs to stay clear, bold and sophisticated.
• Too much on the page, clarity is key for clear communication without trying to clutter too much on the page.

```html
<!DOCTYPE html>
<html lang="en">
<head>
<meta charset="utf-8">
<title>Building and Facilities Management Brochure – Spread</title>
<link rel="stylesheet" href="https://fonts.googleapis.com/css2?family=Kanit:wght@300;400;500;600;700&display=swap">
<style>
  :root {
    --backdrop: #e4e5e7;
    --brand-blue: #1f9be0;
    --brand-blue-light: #4fb8ee;
    --ink-dark: #2f3a4b;
    --ink-body: #3a4454;
    --page-light-top: #dfe6ee;
    --page-light-bottom: #b9c6d3;
    --page-dark-top: #3d4a5c;
    --page-dark-bottom: #1f2835;
    --white: #ffffff;
  }
  * { box-sizing: border-box; margin: 0; padding: 0; }
  html, body { width: 1200px; height: 800px; overflow: hidden; }
  body {
    background: var(--backdrop);
    font-family: "Kanit", sans-serif;
    position: relative;
  }
  .spread {
    position: absolute;
    left: 110px; top: 40px;
    width: 980px; height: 720px;
    display: flex;
    box-shadow: 0 10px 30px rgba(0,0,0,0.18);
  }
  .page { position: relative; width: 490px; height: 720px; overflow: hidden; }

  /* Left page */
  .page-vision { color: var(--ink-body); }
  .page-vision .cityscape {
    position: absolute; inset: 0;
    background: linear-gradient(170deg, var(--page-light-top) 0%, #cfd9e3 45%, var(--page-light-bottom) 100%);
  }
  .swoosh { position: absolute; left: 0; width: 100%; }
  .swoosh-top { top: 0; height: 210px; }
  .vision-content {
    position: absolute; top: 138px; left: 40px; right: 26px; bottom: 16px;
    display: flex; flex-direction: column;
  }
  .vision-title, .aspects-title {
    text-align: center; line-height: 1.15;
    color: var(--brand-blue); font-weight: 600; font-size: 38px;
    text-decoration: underline; text-decoration-thickness: 3px; text-underline-offset: 5px;
  }
  .vision-columns {
    margin-top: 12px;
    display: flex; gap: 16px; font-size: 10px; line-height: 1.3; font-weight: 300;
    color: var(--ink-dark);
  }
  .vision-columns p { flex: 1; border-left: 2px solid var(--ink-dark); padding-left: 7px; text-align: justify; }
  .vision-columns p:first-child { margin-top: 22px; }
  .aspects-title { margin-top: 14px; }
  .aspect-list { margin-top: 10px; list-style: none; }
  .aspect-list li { margin-bottom: 6px; }
  .aspect-name {
    display: block; font-size: 17px; font-weight: 600; color: var(--ink-dark); line-height: 1.1;
    text-decoration: underline; text-decoration-thickness: 2px; text-underline-offset: 3px;
  }
  .aspect-desc { display: block; margin-top: 2px; font-size: 10px; font-weight: 300; line-height: 1.25; color: var(--ink-dark); }

  /* Right page */
  .page-services { color: var(--white); }
  .page-services .skyline {
    position: absolute; inset: 0;
    background: linear-gradient(160deg, var(--page-dark-top) 0%, #2d3848 50%, var(--page-dark-bottom) 100%);
  }
  .services-title {
    position: absolute; top: 30px; width: 100%; text-align: center;
    font-size: 44px; font-weight: 700; letter-spacing: 1px;
    text-decoration: underline; text-decoration-thickness: 3px; text-underline-offset: 6px;
  }
  .service-group { position: absolute; left: 44px; right: 40px; }
  .service-group h2 {
    font-size: 20px; font-weight: 600; line-height: 1.1;
    border-left: 3px solid var(--white); padding-left: 8px;
  }
  .service-group .intro { font-size: 10.5px; font-weight: 300; line-height: 1.3; padding-left: 11px; }
  .core { top: 128px; }
  .core-list {
    list-style: none; display: flex; margin-top: 26px; padding-left: 12px; font-size: 12.5px;
  }
  .core-list li { padding: 0 10px 2px; border-bottom: 1.5px solid var(--white); }
  .core-list li + li { border-left: 1.5px solid var(--white); margin-left: 6px; }
  .value { top: 288px; }
  .value-list {
    list-style: none; display: grid; grid-template-columns: 1fr 1.2fr;
    column-gap: 20px; row-gap: 8px; margin-top: 30px; padding-left: 30px; font-size: 12px;
  }
  .value-list li span { border-bottom: 1.5px solid var(--white); padding-bottom: 1px; }
  .contact-note {
    position: absolute; top: 488px; left: 60px; right: 50px;
    border-top: 1.5px solid var(--white); padding-top: 10px;
    text-align: center; font-size: 11.5px; font-weight: 300; line-height: 1.35;
  }
  .swoosh-bottom { bottom: 0; height: 190px; }
</style>
</head>
<body>
  <main class="spread">
    <section class="page page-vision">
      <div class="cityscape" role="img" aria-label="Faded photograph of city office towers in pale blue tones"></div>
      <svg class="swoosh swoosh-top" viewBox="0 0 490 210" preserveAspectRatio="none" aria-hidden="true">
        <path d="M0 0 H490 V0 C400 30 330 50 260 60 C150 76 60 70 0 96 Z" fill="var(--white)" opacity="0.85"/>
        <path d="M0 96 C60 70 150 76 260 60 C330 50 420 20 490 0 L490 10 C420 40 330 70 250 80 C150 96 70 100 0 128 Z" fill="var(--brand-blue)"/>
        <path d="M0 128 C70 100 150 96 250 80 C330 70 420 40 490 10 L490 16 C420 50 330 82 250 92 C160 104 80 112 0 140 Z" fill="var(--ink-dark)"/>
        <path d="M0 104 C90 150 200 140 330 70 C390 40 440 18 490 6" fill="none" stroke="var(--brand-blue-light)" stroke-width="3"/>
      </svg>

      <div class="vision-content">
        <h1 class="vision-title">Vision</h1>
        <div class="vision-columns">
          <p>At Arden, our aim is to provide complete solutions for Building and Facilities Owners and Strata Corporations in the management of their assets. With the understanding that each property has different needs and requirements, our focus is to work with clients to tailor solutions best suited to their specific needs.</p>
          <p>Our aim is to ensure the Building and Facilities are managed to the highest standards using the latest technological management solutions to efficiently and effectively control all aspects of the building. With a keen focus on controlling costs to ensure funds are spent cost-effectively, through improved operations and management of all aspects of the building.</p>
        </div>

        <h1 class="aspects-title">Key Aspects</h1>
        <ul class="aspect-list">
          <li><span class="aspect-name">Compliance</span><span class="aspect-desc">With relevant industry acts and regulations</span></li>
          <li><span class="aspect-name">OH&amp;S</span><span class="aspect-desc">To ensure the building and aspects are controlled safely and the risk of all contractors and owners is reduced and managed</span></li>
          <li><span class="aspect-name">Preventative Maintenance</span><span class="aspect-desc">To ensure assets are professionally maintained to ensure the best reliability and longevity of each asset.</span></li>
          <li><span class="aspect-name">Reactive Maintenance</span><span class="aspect-desc">To ensure any issues that arise are resolved and handled as efficiently as possible.</span></li>
          <li><span class="aspect-name">Communication</span><span class="aspect-desc">To ensure the Committee and Owners have clear and concise information and knowledge of the aspects of their building and assets.</span></li>
          <li><span class="aspect-name">Relationships</span><span class="aspect-desc">Are a top priority as they are paramount for effective management with Owners, Residents, Developers and Strata Managers</span></li>
        </ul>
      </div>
    </section>

    <section class="page page-services">
      <div class="skyline" role="img" aria-label="Photograph looking up between dark glass skyscrapers with an aeroplane overhead"></div>
      <h1 class="services-title">SERVICES</h1>

      <div class="service-group core">
        <h2>Core Services</h2>
        <p class="intro">These are the core focus of the business to provide the highest standard in Building and Facilities Management</p>
        <ul class="core-list">
          <li>Building Management</li>
          <li>Facilities Management</li>
          <li>Caretaker</li>
        </ul>
      </div>

      <div class="service-group value">
        <h2>Value Added Services</h2>
        <p class="intro">In addition to the Core Service we are proud to offer these Value-Added services to complement the management of the Building, or offer as stand-alone services to assist owners with the management of their Building and Assets.</p>
        <ul class="value-list">
          <li><span>Concierge</span></li>
          <li><span>Handyman</span></li>
          <li><span>Cleaning</span></li>
          <li><span>New Site Setup</span></li>
          <li><span>Electrical</span></li>
          <li><span>Building Defect Management</span></li>
          <li><span>Project Management</span></li>
        </ul>
      </div>

      <p class="contact-note">Please feel free to contact us to enquire about any of the above services either individually or as multiple services to ensure the best value can be provided for your requirements.</p>

      <svg class="swoosh swoosh-bottom" viewBox="0 0 490 190" preserveAspectRatio="none" aria-hidden="true">
        <path d="M0 120 C90 40 240 40 490 90 V190 H0 Z" fill="var(--brand-blue)"/>
        <path d="M0 132 C100 58 250 58 490 104 V190 H0 Z" fill="var(--ink-dark)"/>
        <path d="M0 140 C100 70 250 70 490 112 V190 H0 Z" fill="var(--brand-blue-light)"/>
        <path d="M0 150 C110 84 260 84 490 124 V190 H0 Z" fill="var(--white)"/>
      </svg>
    </section>
  </main>
</body>
</html>
```